Website design: Mobile Physiotherapy, Massage & Personal Training Business

I need a website that reflects a staff of health and fitness professionals. I would like the theme of the website to match the company logo (Harbor Motion Wellness).
This is a link for a competitors website that I am fond of:
http://www.tandrilcare.example.au/
I am open to any and all creative and innovative designs.

Industry/Entity Type

Fitness

```html
<!DOCTYPE html>
<html lang="en">
<head>
<meta charset="utf-8">
<title>Harbor Motion Wellness</title>
<link href="https://fonts.googleapis.com/css2?family=Open+Sans:ital,wght@0,300;0,400;0,600;0,700;1,400&display=swap" rel="stylesheet">
<style>
:root{
  --red:#e8414f;
  --red-dark:#c42d3b;
  --ink:#333;
  --muted:#888;
  --light:#f4f4f4;
  --line:#dcdcdc;
  --slate:#4d4d4d;
  --white:#fff;
  --track-light:#f1f1f1;
  --track-mid:#a9a9a9;
  --track-dark:#5c5c5c;
}
*{box-sizing:border-box;margin:0;padding:0}
html,body{width:1200px;height:3900px;overflow:hidden}
body{font-family:"Open Sans",Arial,sans-serif;color:var(--ink);background:var(--white);position:relative;font-size:13px;line-height:1.6}
section,header,footer{position:absolute;left:0;width:1200px}
.wrap{position:absolute;left:180px;width:840px}
.fill{background:linear-gradient(135deg,#cfcfcf,#9c9c9c)}
.section-title{font-weight:400;font-size:26px;letter-spacing:.5px;text-transform:uppercase;color:#333}
.section-title.center{text-align:center}
.rule{width:40px;height:2px;background:var(--red);margin:10px 0 20px}
p.copy{color:var(--muted);font-size:13px;line-height:1.7}
.btn{display:inline-block;background:var(--red);color:#fff;font-size:12px;font-weight:600;padding:7px 16px;border-radius:2px}
.arrows{display:flex;gap:8px}
.arrow{width:30px;height:30px;border:1px solid rgba(255,255,255,.8);display:flex;align-items:center;justify-content:center}
.arrow svg{width:12px;height:12px}

/* header */
.hero{top:0;height:600px;background:var(--track-mid)}
.hero .photo{position:absolute;inset:0;
  background:
    radial-gradient(ellipse 170px 230px at 560px 330px,rgba(232,65,79,.85),rgba(232,65,79,.35) 55%,transparent 100%),
    radial-gradient(ellipse 420px 140px at 780px 250px,rgba(255,255,255,.55),transparent 70%),
    linear-gradient(172deg,var(--track-light) 0%,#dedede 30%,#b9b9b9 48%,#7d7d7d 72%,var(--track-dark) 100%);}
.hero .photo::after{content:"";position:absolute;left:0;right:0;bottom:0;height:120px;background:linear-gradient(180deg,transparent,rgba(40,40,40,.35))}
.brand{position:absolute;left:180px;top:18px;display:flex;align-items:center;gap:10px;background:rgba(255,255,255,.95);padding:10px 14px;z-index:2}
.brand .dot{width:22px;height:22px;border-radius:50%;background:var(--red)}
.brand span{font-weight:700;font-size:18px;color:var(--red)}
.nav{position:absolute;left:560px;top:40px;height:40px;display:flex;background:#fff;z-index:2}
.nav a{font-size:12px;font-weight:600;color:#555;padding:0 14px;line-height:40px;text-decoration:none}
.nav a.active{background:var(--red);color:#fff}
.dropdown{position:absolute;left:780px;top:80px;width:170px;background:var(--red);z-index:2}
.dropdown div{color:#fff;font-size:11px;font-weight:600;padding:9px 14px;border-bottom:1px solid rgba(255,255,255,.25)}

/* about */
.about{top:600px;height:340px;background:var(--light)}
.about .text{left:180px;top:40px;width:400px}
.about .video{position:absolute;left:620px;top:32px;width:400px;height:228px;background:linear-gradient(135deg,#8a8a8a,#c9c9c9)}
.video .play{position:absolute;left:170px;top:84px;width:60px;height:42px;background:var(--red);border-radius:8px;display:flex;align-items:center;justify-content:center}
.video .bar{position:absolute;left:0;right:0;bottom:0;height:22px;background:rgba(0,0,0,.75)}
.video .bar i{position:absolute;left:40px;top:10px;width:300px;height:3px;background:#777}
.video .bar i::before{content:"";position:absolute;left:0;top:0;width:60px;height:3px;background:var(--red)}

/* red bands */
.band{height:360px;background:var(--red)}
.services{top:940px}
.products{top:2500px}
.band .intro{position:absolute;left:180px;top:52px;width:200px;height:288px;background:var(--red-dark);color:#fff;padding:26px 20px}
.intro h3{font-size:14px;font-weight:600;text-transform:uppercase}
.intro .rule{background:#fff;margin:8px 0 12px}
.intro p{font-size:11px;line-height:1.5;opacity:.9;margin-bottom:22px}
.card{position:absolute;top:52px;width:190px;height:288px;background:#fff}
.card .img{height:208px;margin:0}
.card .caption{text-align:center;font-size:13px;color:#444;line-height:80px}
.c1{left:400px}.c2{left:612px}.c3{left:830px}

/* news */
.news{top:1300px;height:500px;background:#fff}
.col{position:absolute;top:70px;width:400px}
.col.left{left:180px}.col.right{left:620px}
.date{font-size:11px;color:var(--muted);margin-bottom:4px}
.news-title{color:var(--red);font-size:24px;font-weight:400;line-height:1.3;margin-bottom:14px}
.tips li{list-style:none;margin-bottom:14px}
.tips li strong{display:block;color:var(--red);font-weight:400;font-size:15px}
.tips li strong::before{content:"• ";}
.tips li span{display:block;color:var(--muted);font-size:11px;padding-left:12px}

/* team */
.team{top:1800px;height:300px;background:var(--slate)}
.team .intro{position:absolute;left:180px;top:48px;width:200px;height:210px;background:var(--red);color:#fff;padding:22px 20px}
.team .photo{position:absolute;left:400px;top:48px;width:190px;height:210px;background:linear-gradient(135deg,#9a9a9a,#d6d6d6)}
.team .profile{position:absolute;left:610px;top:48px;width:410px;height:210px;background:#fff;padding:22px 24px}
.profile h4{font-size:14px;font-weight:600;text-transform:uppercase}
.profile .rule{margin:8px 0 14px}

/* testimonials */
.testimonials{top:2100px;height:400px;background:var(--light)}
.testimonials .section-title{position:absolute;top:30px;width:1200px}
.avatar{position:absolute;left:560px;top:100px;width:80px;height:80px;border-radius:50%;background:linear-gradient(135deg,#c99f7a,#8a6a50);border:3px solid #fff}
.quote{position:absolute;left:260px;top:210px;width:680px;text-align:center;font-style:italic;color:#666;font-size:16px;line-height:1.6}
.author{position:absolute;top:310px;width:1200px;text-align:center;font-weight:600;font-size:13px}
.side-arrow{position:absolute;top:212px;width:30px;height:30px;border:1px solid #bbb;background:#fff;display:flex;align-items:center;justify-content:center}
.side-arrow svg{width:12px;height:12px}
.testimonials .sa-l{left:180px}.testimonials .sa-r{left:990px}

/* location */
.location{top:2860px;height:490px;background:#fff}
.location .section-title{position:absolute;top:40px;width:1200px}
.map{position:absolute;left:180px;top:110px;width:400px;height:300px;background:linear-gradient(135deg,#d9e4cc,#b8cde0)}
.contact{position:absolute;left:700px;top:116px;width:320px}
.contact h3{font-size:22px;font-weight:400;margin-bottom:14px}
.contact .row{display:flex;align-items:center;gap:10px;font-size:12px;color:#666;margin-bottom:8px}
.contact .row svg{width:14px;height:14px;flex:none}
.contact .btn{margin-top:12px}

/* associates */
.associates{top:3350px;height:250px;background:var(--light)}
.associates .section-title{position:absolute;top:24px;width:1200px}
.badges{position:absolute;left:250px;top:110px;width:700px;display:flex;justify-content:space-between}
.badge{width:90px;height:90px;border-radius:50%}
.associates .side-arrow{top:140px}
.associates .sa-l{left:180px}.associates .sa-r{left:990px}

/* footer */
.site-footer{top:3600px;height:260px;background:#fff;border-top:1px solid var(--line)}
.fcol{position:absolute;top:34px}
.fcol h5{font-size:11px;font-weight:700;text-transform:uppercase;margin-bottom:10px}
.fcol li{list-style:none;font-size:11px;color:#777;margin-bottom:6px}
.fcol li::before{content:"›  ";color:var(--red)}
.f-brand{left:180px;width:200px}
.f-brand .brand-mark{display:flex;align-items:center;gap:8px;margin-bottom:10px}
.f-brand .dot{width:18px;height:18px;border-radius:50%;background:var(--red)}
.f-brand .brand-mark span{color:var(--red);font-weight:700;font-size:14px}
.f-news{left:400px;width:200px}
.f-gallery{left:620px;width:180px}
.thumbs{display:grid;grid-template-columns:repeat(3,52px);gap:6px}
.thumbs div{height:44px;background:linear-gradient(135deg,#bbb,#888)}
.f-links{left:820px;width:200px}
.bottom-bar{position:absolute;left:0;width:1200px;top:3860px;height:40px;background:#ececec;font-size:11px;color:#888}
.bottom-bar .copy{position:absolute;left:180px;top:12px}
.socials{position:absolute;left:880px;top:11px;display:flex;gap:8px}
.socials i{width:18px;height:18px;border-radius:50%;background:#bbb;display:block}
</style>
</head>
<body>

<header class="hero">
  <div class="photo" role="img" aria-label="Sprinter in red bursting from starting blocks on a grey stadium running track"></div>
  <div class="brand"><div class="dot"></div><span>Harbor Motion Wellness</span></div>
  <nav class="nav">
    <a class="active">HOME</a><a>ABOUT</a><a>SERVICES</a><a>PRODUCTS</a><a>MORE</a><a>CONTACT</a><a>LOG IN</a>
  </nav>
  <div class="dropdown">
    <div>LOREM IPSUM DOLOR</div><div>LOREM IPSUM DOLOR</div><div>LOREM IPSUM DOLOR</div><div>LOREM IPSUM DOLOR</div><div>LOREM IPSUM DOLOR</div>
  </div>
</header>

<section class="about">
  <div class="wrap text">
    <h2 class="section-title">About</h2>
    <div class="rule"></div>
    <p class="copy">Duis autem vel eum iriure dolor in hendrerit in vulputate velit esse molestie consequat, vel illum dolore eu feugiat nulla facilisis at vero eros et accumsan et iusto odio dignissim.</p>
    <p class="copy" style="margin-top:12px">Nam liber tempor cum soluta nobis eleifend option congue nihil imperdiet doming id quod mazim placerat facer possim assum. Typi non habent claritatem insitam est usus legentis in iis qui facit eorum claritatem.</p>
  </div>
  <div class="video" role="img" aria-label="Video still of a trainer in a gym">
    <div class="play"><svg width="18" height="18" viewBox="0 0 18 18"><path d="M4 2 L16 9 L4 16Z" fill="#fff"/></svg></div>
    <div class="bar"><i></i></div>
  </div>
</section>

<section class="band services">
  <div class="intro">
    <h3>Our Services</h3><div class="rule"></div>
    <p>Lorem ipsum dolor sit amet consectetuer adipiscing elit.</p>
    <div class="arrows">
      <div class="arrow"><svg viewBox="0 0 12 12"><path d="M8 1 L3 6 L8 11" stroke="#fff" stroke-width="2" fill="none"/></svg></div>
      <div class="arrow"><svg viewBox="0 0 12 12"><path d="M4 1 L9 6 L4 11" stroke="#fff" stroke-width="2" fill="none"/></svg></div>
    </div>
  </div>
  <div class="card c1"><div class="img fill" role="img" aria-label="Physiotherapist treating a knee"></div><div class="caption">Sports Physio</div></div>
  <div class="card c2"><div class="img fill" role="img" aria-label="Hands holding a red apple and measuring tape"></div><div class="caption">Sports Nutrition</div></div>
  <div class="card c3"><div class="img fill" role="img" aria-label="Foot being massaged"></div><div class="caption">Podiatry</div></div>
</section>

<section class="news">
  <div class="col left">
    <h2 class="section-title">Latest News</h2><div class="rule"></div>
    <div class="date">May 20, 2013</div>
    <h3 class="news-title">Typi Non Habent Claritatem Insitam Est Usus</h3>
    <p class="copy">Duis autem vel eum iriure dolor in hendrerit in vulputate velit esse molestie consequat, vel illum dolore eu feugiat nulla facilisis at vero eros et accumsan et iusto odio dignissim qui blandit praesent luptatum.</p>
    <a class="btn" style="margin-top:22px">Read More</a>
  </div>
  <div class="col right">
    <h2 class="section-title">Pro Health Tips</h2><div class="rule"></div>
    <ul class="tips">
      <li><strong>Claritas Est Etiam Processu</strong><span>Duis autem vel eum iriure dolor in hendrerit in vulputate velit esse molestie consequat.</span></li>
      <li><strong>Lorem Ipsum Dolor Sit Amet</strong><span>Duis autem vel eum iriure dolor in hendrerit in vulputate velit esse molestie consequat.</span></li>
    </ul>
    <a class="btn" style="margin-top:10px">Read More</a>
  </div>
</section>

<section class="team">
  <div class="intro">
    <h3>Our Team</h3><div class="rule"></div>
    <p>Lorem ipsum</p>
    <div class="arrows">
      <div class="arrow"><svg viewBox="0 0 12 12"><path d="M8 1 L3 6 L8 11" stroke="#fff" stroke-width="2" fill="none"/></svg></div>
      <div class="arrow"><svg viewBox="0 0 12 12"><path d="M4 1 L9 6 L4 11" stroke="#fff" stroke-width="2" fill="none"/></svg></div>
    </div>
  </div>
  <div class="photo" role="img" aria-label="Portrait of a team trainer in a gym"></div>
  <div class="profile">
    <h4>Claire Ashworth</h4><div class="rule"></div>
    <p class="copy">Duis autem vel eum iriure dolor in hendrerit in vulputate velit esse molestie consequat, vel illum dolore eu feugiat nulla facilisis at vero eros et accumsan et iusto odio dignissim.</p>
  </div>
</section>

<section class="testimonials">
  <h2 class="section-title center">Testimonials</h2>
  <div class="avatar" role="img" aria-label="Client portrait"></div>
  <div class="side-arrow sa-l"><svg viewBox="0 0 12 12"><path d="M8 1 L3 6 L8 11" stroke="#999" stroke-width="2" fill="none"/></svg></div>
  <p class="quote">Ut wisi enim ad minim veniam, quis nostrud exerci tation ullamcorper suscipit lobortis nisl ut aliquip ex ea commodo consequat.</p>
  <div class="side-arrow sa-r"><svg viewBox="0 0 12 12"><path d="M4 1 L9 6 L4 11" stroke="#999" stroke-width="2" fill="none"/></svg></div>
  <div class="author">Daniel Whitcombe</div>
</section>

<section class="band products">
  <div class="intro">
    <h3>Our Products</h3><div class="rule"></div>
    <p>Lorem ipsum dolor sit amet consectetuer adipiscing elit.</p>
    <div class="arrows">
      <div class="arrow"><svg viewBox="0 0 12 12"><path d="M8 1 L3 6 L8 11" stroke="#fff" stroke-width="2" fill="none"/></svg></div>
      <div class="arrow"><svg viewBox="0 0 12 12"><path d="M4 1 L9 6 L4 11" stroke="#fff" stroke-width="2" fill="none"/></svg></div>
    </div>
  </div>
  <div class="card c1"><div class="img fill" role="img" aria-label="Black ankle brace"></div><div class="caption">Braces &amp; Tape</div></div>
  <div class="card c2"><div class="img fill" role="img" aria-label="Woman exercising on a fitness ball"></div><div class="caption">Exercise Equipments</div></div>
  <div class="card c3"><div class="img fill" role="img" aria-label="Person resting on a supportive pillow"></div><div class="caption">Postural Aids</div></div>
</section>

<section class="location">
  <h2 class="section-title center">Our Location</h2>
  <div class="map" role="img" aria-label="Street map of the clinic area"></div>
  <div class="contact">
    <h3>Harbor Motion Wellness</h3>
    <div class="row"><svg viewBox="0 0 14 14"><path d="M3 1 L5 1 L6 4 L4.5 5 A7 7 0 0 0 9 9.5 L10 8 L13 9 L13 11 A2 2 0 0 1 11 13 A10 10 0 0 1 1 3 A2 2 0 0 1 3 1Z" fill="#e8414f"/></svg>(08) 5550 1472</div>
    <div class="row"><svg viewBox="0 0 14 14"><rect x="1" y="3" width="12" height="8" fill="none" stroke="#e8414f" stroke-width="1.4"/><path d="M1 3 L7 8 L13 3" fill="none" stroke="#e8414f" stroke-width="1.4"/></svg>hello@harbormotion.example.au</div>
    <div class="row"><svg viewBox="0 0 14 14"><path d="M7 13 C3 8 2 6 2 5 A5 5 0 0 1 12 5 C12 6 11 8 7 13Z" fill="#e8414f"/><circle cx="7" cy="5" r="1.8" fill="#fff"/></svg>48 Lantern Quay Rd,<br>Eastvale Harbour</div>
    <a class="btn">Get Directions</a>
  </div>
</section>

<section class="associates">
  <h2 class="section-title center">Our Associates</h2>
  <div class="side-arrow sa-l"><svg viewBox="0 0 12 12"><path d="M8 1 L3 6 L8 11" stroke="#999" stroke-width="2" fill="none"/></svg></div>
  <div class="badges">
    <div class="badge" style="background:#2a8fc9"></div>
    <div class="badge" style="background:#f2a23a"></div>
    <div class="badge" style="background:#3f5f3a"></div>
    <div class="badge" style="background:#2a9a7a"></div>
    <div class="badge" style="background:#e6b43a"></div>
  </div>
  <div class="side-arrow sa-r"><svg viewBox="0 0 12 12"><path d="M4 1 L9 6 L4 11" stroke="#999" stroke-width="2" fill="none"/></svg></div>
</section>

<footer class="site-footer">
  <div class="fcol f-brand">
    <div class="brand-mark"><div class="dot"></div><span>Harbor Motion Wellness</span></div>
    <p class="copy" style="font-size:11px">Typi non habent claritatem insitam, est usus legentis in iis qui facit eorum claritatem. Investigationes demonstraverunt.</p>
  </div>
  <div class="fcol f-news">
    <h5>Latest News</h5>
    <ul><li>Typi non habent claritatem</li><li>Claritas est etiam processus</li><li>Lorem ipsum dolor sit amet</li><li>Mirum est notare quam</li></ul>
  </div>
  <div class="fcol f-gallery">
    <h5>Gallery</h5>
    <div class="thumbs" role="img" aria-label="Gallery thumbnails of training sessions"><div></div><div></div><div></div><div></div><div></div><div></div></div>
  </div>
  <div class="fcol f-links">
    <h5>Links</h5>
    <ul><li>Log In / Register</li><li>Privacy Policy</li><li>Terms and Conditions</li></ul>
  </div>
</footer>

<div class="bottom-bar">
  <span class="copy">© Copyright Harbor Motion Wellness</span>
  <div class="socials"><i></i><i></i><i></i><i></i><i></i></div>
</div>

</body>
</html>
```